National appliance rental company needs a newspaper ad design

We need an ad template that we can use for different newspaper advertising. Ad is to be colourful - I have attached our current marketing so you have an idea of colours.
Text to be something like the below:

Want it, Rent it, Own it!

Need to update your furniture? Kids need stuff for school?

(Put in pics of phones and TV)

Tabvos starting from just $8 per week
Smart phones starting from $10 per week
Large family fridges from $30 per week

TV’s, laptops, whitegoods, furniture, beds – we will finance just about anything!

Fast approvals – call 1300 582 967 or go to www.koralinehiregroup.com.au/apply - NOW!
$50 credit voucher given to the first 10 successful applicants.

(Pic of logo somewhere)
Terms and conditions apply. Pricing based on 24 month term

Koraline Hire Group P/L ACN 061 774 298. Australian Credit Licence # 718249

Target Market(s)

Low income people and families

Industry/Entity Type

Appliance

Requirements
Must have
• I would love to have a couple of different sizes.
• Maybe 6cm x 10 cm, and also 10cms x 10cms.
Nice to have
• Please use the green from fridge magnet and colours from our logo, etc.

```html
<!DOCTYPE html>
<html lang="en">
<head>
<meta charset="utf-8">
<title>Koraline Hire Group – Want it, Rent it, Own it!</title>
<link rel="stylesheet" href="https://fonts.googleapis.com/css2?family=Bebas+Neue&family=Open+Sans:ital,wght@0,400;0,700;1,700&display=swap">
<style>
  :root {
    --lime: #a3d34b;
    --lime-deep: #93c63e;
    --crimson: #e8174a;
    --red-disc: #c8102e;
    --blue: #2d6cc2;
    --blue-deep: #1d4f9c;
    --navy-text: #1c4e9e;
    --white: #ffffff;
    --silver: #d4d7db;
    --ink: #1a1a1a;
  }
  * { margin: 0; padding: 0; box-sizing: border-box; }
  html, body { width: 799px; height: 1200px; overflow: hidden; }
  body { background: var(--lime); font-family: "Bebas Neue", "Arial Narrow", sans-serif; }

  .ad {
    position: relative;
    width: 799px;
    height: 1200px;
    background: radial-gradient(ellipse at 50% 40%, var(--lime) 0%, var(--lime-deep) 100%);
    overflow: hidden;
  }

  .brand {
    position: absolute;
    left: 28px; top: 150px;
    width: 330px;
  }
  .brand__row { display: flex; align-items: center; gap: 10px; }
  .brand__mark { width: 30px; height: 30px; background: var(--white); flex: none; }
  .brand__name { font-size: 44px; line-height: 1; color: var(--crimson); }
  .brand__tagline {
    margin-top: 8px; padding-left: 40px;
    font-family: "Open Sans", Arial, sans-serif;
    font-style: italic; font-weight: 700; font-size: 13px; color: var(--ink);
  }

  .headline {
    position: absolute;
    left: 377px; top: 18px;
    font-size: 132px; line-height: 108px;
    color: var(--crimson);
    letter-spacing: 1px;
  }

  .question-pill {
    position: absolute;
    left: 63px; top: 364px;
    width: 674px; height: 163px;
    border-radius: 52px;
    background: linear-gradient(180deg, #4b8be0 0%, var(--blue) 45%, var(--blue-deep) 100%);
    box-shadow: 0 10px 18px rgba(0,0,0,.25);
    display: flex; flex-direction: column; justify-content: center; align-items: center;
    color: var(--white); font-size: 50px; line-height: 54px; text-align: center;
  }

  .offer__label {
    position: absolute; top: 556px; width: 200px;
    color: var(--white); font-size: 29px; line-height: 28px; text-align: center;
    text-shadow: 0 2px 3px rgba(0,0,0,.35);
  }
  .offer__disc { position: absolute; width: 190px; height: 190px; }
  .offer__price {
    position: absolute; width: 150px; text-align: center; color: var(--white);
  }
  .offer__amount { font-size: 86px; line-height: 80px; }
  .offer__amount sup { font-size: 34px; vertical-align: 36px; margin-right: 2px; }
  .offer__unit { font-size: 18px; line-height: 18px; }
  .product { position: absolute; border-radius: 6px; }
  .product--tablet { left: 23px; top: 651px; width: 104px; height: 140px; background: linear-gradient(160deg,#f4f4f4,#d9dde2); border: 2px solid #c6c9cd; }
  .product--phone { left: 300px; top: 651px; width: 78px; height: 150px; background: linear-gradient(160deg,#3a6fb8,#1f2328 60%); border-radius: 12px; }
  .product--fridge { left: 537px; top: 645px; width: 104px; height: 168px; background: linear-gradient(90deg,#8d9399,#c9cdd1 50%,#7d8389); border-radius: 4px; }

  .approvals {
    position: absolute; left: 91px; top: 851px; width: 605px; height: 88px;
    border: 3px solid var(--white); border-radius: 10px;
    display: flex; align-items: center; justify-content: center; padding-left: 70px;
    color: var(--crimson); font-size: 72px; line-height: 1;
  }
  .approvals__tick { position: absolute; left: 86px; top: 846px; width: 100px; height: 100px; }

  .contact {
    position: absolute; left: 0; top: 958px; width: 799px; text-align: center;
    color: var(--navy-text); font-size: 29px; line-height: 40px;
  }
  .legal {
    position: absolute; left: 0; top: 1116px; width: 799px; text-align: center;
    color: var(--white); font-family: "Open Sans", Arial, sans-serif; font-size: 18px; line-height: 29px;
  }
</style>
</head>
<body>
<main class="ad">

  <div class="brand">
    <div class="brand__row">
      <span class="brand__mark"></span>
      <span class="brand__name">Koraline Hire Group</span>
    </div>
    <p class="brand__tagline">“It’s cheaper to hire local!”</p>
  </div>

  <h1 class="headline">WANT IT,<br>RENT IT,<br>OWN IT!</h1>

  <div class="question-pill">
    <p>NEED TO UPDATE YOUR FURNITURE?</p>
    <p>KIDS NEED STUFF FOR SCHOOL?</p>
  </div>

  <!-- Offer 1 -->
  <p class="offer__label" style="left:50px;">TABVOS STARTING<br>FROM JUST</p>
  <svg class="offer__disc" style="left:93px; top:625px;" viewBox="0 0 190 190" aria-hidden="true">
    <defs>
      <linearGradient id="ring" x1="0" y1="0" x2="1" y2="1">
        <stop offset="0" stop-color="#f5f6f7"/><stop offset=".5" stop-color="#a9adb2"/><stop offset="1" stop-color="#e6e8ea"/>
      </linearGradient>
    </defs>
    <circle cx="95" cy="95" r="90" fill="url(#ring)"/>
    <circle cx="95" cy="95" r="77" fill="#c8102e"/>
  </svg>
  <div class="product product--tablet" role="img" aria-label="Photo of a white tablet computer"></div>
  <div class="offer__price" style="left:135px; top:665px;">
    <div class="offer__amount"><sup>$</sup>8</div>
    <div class="offer__unit">PER WEEK</div>
  </div>

  <!-- Offer 2 -->
  <p class="offer__label" style="left:305px;">SMART PHONES<br>STARTING FROM</p>
  <svg class="offer__disc" style="left:327px; top:625px;" viewBox="0 0 190 190" aria-hidden="true">
    <circle cx="95" cy="95" r="90" fill="url(#ring)"/>
    <circle cx="95" cy="95" r="77" fill="#c8102e"/>
  </svg>
  <div class="product product--phone" role="img" aria-label="Photo of a smartphone"></div>
  <div class="offer__price" style="left:372px; top:665px;">
    <div class="offer__amount"><sup>$</sup>10</div>
    <div class="offer__unit">PER WEEK</div>
  </div>

  <!-- Offer 3 -->
  <p class="offer__label" style="left:565px;">LARGE FAMILY<br>FRIDGES FROM</p>
  <svg class="offer__disc" style="left:560px; top:625px;" viewBox="0 0 190 190" aria-hidden="true">
    <circle cx="95" cy="95" r="90" fill="url(#ring)"/>
    <circle cx="95" cy="95" r="77" fill="#c8102e"/>
  </svg>
  <div class="product product--fridge" role="img" aria-label="Photo of a stainless steel side-by-side fridge"></div>
  <div class="offer__price" style="left:605px; top:665px;">
    <div class="offer__amount"><sup>$</sup>30</div>
    <div class="offer__unit">PER WEEK</div>
  </div>

  <div class="approvals">FAST APPROVALS</div>
  <svg class="approvals__tick" viewBox="0 0 100 100" aria-hidden="true">
    <circle cx="50" cy="52" r="42" fill="#ffffff" stroke="#2d8fd6" stroke-width="8"/>
    <path d="M28 52 L45 70 L92 14" fill="none" stroke="#e8174a" stroke-width="12" stroke-linecap="round" stroke-linejoin="round"/>
  </svg>

  <div class="contact">
    <p>CALL 1300 582 967 OR GO TO</p>
    <p>WWW.KORALINEHIREGROUP.COM.AU/APPLY</p>
    <p>$50 CREDIT VOUCHER GIVEN TO THE FIRST 10 SUCCESSFUL APPLICANTS.</p>
  </div>

  <div class="legal">
    <p>Terms and conditions apply. Pricing based on 24 month term</p>
    <p>Koraline Hire Group P/L ACN 061 774 298. Australian Credit Licence # 718249</p>
  </div>

</main>
</body>
</html>
```